Ashford Vale Crematory
Harlow Springs, MI
Project: Ashford Vale Crematory
Ashford Vale Crematory -
Creative Brief
Simple
Paul Dorsey III
2873 Fennel St. Harlow Springs, MI 58317
harlowbrenton@examplemail.net

```html
<!DOCTYPE html>
<html lang="en">
<head>
<meta charset="utf-8">
<title>Ashford Vale Crematory — Stationery Set</title>
<link href="https://fonts.googleapis.com/css2?family=Cormorant+Garamond:wght@600&family=Open+Sans:wght@400&display=swap" rel="stylesheet">
<style>
  :root {
    --backdrop: #7b7c80;
    --paper: #ffffff;
    --navy: #2f3568;
    --rule: #c9cbd6;
    --ink: #4a4d5e;
    --faint: #eef0f4;
  }
  * { box-sizing: border-box; margin: 0; padding: 0; }
  html, body { width: 1200px; height: 626px; overflow: hidden; }
  body { background: var(--backdrop); position: relative; font-family: "Open Sans", sans-serif; color: var(--ink); }
  .sheet { position: absolute; background: var(--paper); overflow: hidden; }
  .sheet svg.band { position: absolute; left: 0; top: 0; width: 100%; height: 100%; }
  .brand { position: absolute; display: flex; align-items: center; gap: 5px; }
  .brand-dot { border-radius: 50%; background: var(--navy); flex: none; }
  .brand-name { font-family: "Cormorant Garamond", serif; font-weight: 600; color: var(--navy); white-space: nowrap; }
  .contact { position: absolute; font-size: 5.5px; line-height: 8px; color: var(--ink); white-space: nowrap; }
  .seal { position: absolute; border-radius: 50%; background: var(--faint); }

  .business-card { left: 24px; top: 307px; width: 192px; height: 125px; }
  .business-card .brand { left: 10px; top: 47px; }
  .business-card .brand-dot { width: 14px; height: 14px; }
  .business-card .brand-name { font-size: 8px; }
  .business-card .contact { left: 12px; top: 72px; font-size: 5px; line-height: 7px; }
  .business-card .contact .person { color: var(--navy); }
  .business-card .tagline { position: absolute; right: 12px; bottom: 18px; font-size: 5px; color: var(--navy); }

  .letterhead { left: 233px; top: 31px; width: 403px; height: 576px; }
  .letterhead .brand { left: 18px; top: 26px; }
  .letterhead .brand-dot { width: 20px; height: 20px; }
  .letterhead .brand-name { font-size: 10px; }
  .letterhead .seal { left: 100px; top: 180px; width: 210px; height: 210px; }
  .letterhead .contact { left: 22px; top: 490px; }

  .envelope-back { left: 682px; top: 79px; width: 494px; height: 252px; }

  .envelope-front { left: 682px; top: 338px; width: 494px; height: 264px; }
  .envelope-front .brand { left: 20px; top: 26px; }
  .envelope-front .brand-dot { width: 18px; height: 18px; }
  .envelope-front .brand-name { font-size: 9.5px; }
  .envelope-front .contact { left: 22px; top: 80px; }
  .envelope-front .seal { left: 300px; top: 50px; width: 170px; height: 170px; }
</style>
</head>
<body>

  <section class="sheet business-card" aria-label="Business card">
    <svg class="band" viewBox="0 0 192 125" preserveAspectRatio="none" aria-hidden="true">
      <path d="M0,0 H192 V38 C130,12 60,30 0,44 Z" fill="var(--navy)"/>
      <path d="M0,47 C60,33 130,16 192,42" fill="none" stroke="var(--rule)" stroke-width="0.8"/>
    </svg>
    <div class="brand">
      <span class="brand-dot"></span><span class="brand-name">Ashford Vale Crematory</span>
    </div>
    <div class="contact">
      <div class="person">Harlow Brenton</div>
      <div>Funeral Director</div>
      <div>P: (231) 555-0142</div>
      <div>F: (231) 555-0143</div>
      <div>harlowbrenton@examplemail.net</div>
    </div>
    <div class="tagline">Open Daily</div>
  </section>

  <section class="sheet letterhead" aria-label="Letterhead">
    <svg class="band" viewBox="0 0 403 576" preserveAspectRatio="none" aria-hidden="true">
      <path d="M0,0 H403 V92 C300,30 170,10 0,16 Z" fill="var(--navy)"/>
      <path d="M0,22 C170,16 300,38 403,100" fill="none" stroke="var(--rule)" stroke-width="1"/>
    </svg>
    <div class="brand">
      <span class="brand-dot"></span><span class="brand-name">Ashford Vale Crematory</span>
    </div>
    <div class="seal" role="img" aria-label="Faint circular emblem area"></div>
    <div class="contact">
      <div>P: (231) 555-0142</div>
      <div>F: (231) 555-0143</div>
      <div>harlowbrenton@examplemail.net</div>
      <div>2873 Fennel St. Harlow Springs, MI 58317</div>
    </div>
  </section>

  <section class="sheet envelope-back" aria-label="Envelope back">
    <svg class="band" viewBox="0 0 494 252" preserveAspectRatio="none" aria-hidden="true">
      <path d="M0,0 H494 V70 C420,100 300,104 247,104 C190,104 70,100 0,70 Z" fill="var(--navy)"/>
      <path d="M0,74 C70,104 190,108 247,108 C300,108 420,104 494,74" fill="none" stroke="var(--rule)" stroke-width="1"/>
    </svg>
  </section>

  <section class="sheet envelope-front" aria-label="Envelope front">
    <svg class="band" viewBox="0 0 494 264" preserveAspectRatio="none" aria-hidden="true">
      <path d="M0,0 H494 V40 C360,8 180,4 0,16 Z" fill="var(--navy)"/>
      <path d="M0,21 C180,9 360,14 494,46" fill="none" stroke="var(--rule)" stroke-width="1"/>
    </svg>
    <div class="brand">
      <span class="brand-dot"></span><span class="brand-name">Ashford Vale Crematory</span>
    </div>
    <div class="seal" role="img" aria-label="Faint circular emblem area"></div>
    <div class="contact">
      <div>P: (231) 555-0142</div>
      <div>F: (231) 555-0143</div>
      <div>harlowbrenton@examplemail.net</div>
      <div>2873 Fennel St. Harlow Springs, MI 58317</div>
    </div>
  </section>

</body>
</html>
```